BRAVEN POWERLINE SERVICES needs a vibrant design for electrical contracting work.

I require a card design for my own electrical contracting business. I will be doing a lot of domestic and commercial work, including things such as repairs, maintenance, lighting, installations and various others. LED lighting and energy efficiency will be a big part of my business. I wish not to have childish pictures such as light bulbs in the design, but rather a smart and modern looking card which incorporates my logo colours and perhaps the same lighting strike within the faded background of the card.

Target Market(s)

Residential and Commercial property owners.

Industry/Entity Type

Electrical

Contact Information for Business Card

Dalen Voskic
EC40923
Phone Number: 0417 358 942
Email: dalen@bravenpowerline.com

Font styles to use
Serif
Sans Serif

Requirements
Must have
• My Logo and associated colours.
Nice to have
• Some form of shapes splitting the card into different colours related to the colours of my logo. Electric Blue, Silver/Grey and White.
Should not have
• Childish pictures and symbols such as light bulbs.

```html
<!DOCTYPE html>
<html lang="en">
<head>
<meta charset="utf-8">
<title>Braven Powerline Services – Business Card</title>
<link rel="stylesheet" href="https://fonts.googleapis.com/css2?family=Saira:wght@400;500;700&display=swap">
<style>
  :root {
    --electric-blue: #2222e0;
    --silver: #b9bbc0;
    --silver-dark: #9a9ca2;
    --white: #ffffff;
    --backdrop: #e4e5e8;
    --ink-light: #ffffff;
  }
  * { box-sizing: border-box; margin: 0; padding: 0; }
  html, body {
    width: 1200px; height: 771px; overflow: hidden;
    background: var(--backdrop);
    font-family: "Saira", sans-serif;
  }
  .sheet { position: relative; width: 1200px; height: 771px; }
  .card {
    position: absolute; top: 231px;
    width: 540px; height: 309px;
    background: var(--white);
    box-shadow: 0 4px 18px rgba(0,0,0,.15);
    overflow: hidden;
  }
  .card--brand { left: 40px; }
  .card--contact { left: 620px; }

  .brand-mark {
    position: absolute; display: flex; align-items: center; gap: 16px;
  }
  .card--brand .brand-mark { left: 50%; top: 50%; transform: translate(-50%, -50%); }
  .brand-mark__dot {
    flex: none; border-radius: 50%; background: var(--silver);
  }
  .card--brand .brand-mark__dot { width: 64px; height: 64px; }
  .brand-mark__name {
    color: var(--electric-blue); font-weight: 700; text-transform: uppercase;
    line-height: 1.05; letter-spacing: .02em;
  }
  .card--brand .brand-mark__name { font-size: 28px; }

  .card--contact .brand-mark { right: 22px; top: 40px; gap: 10px; }
  .card--contact .brand-mark__dot { width: 34px; height: 34px; }
  .card--contact .brand-mark__name { font-size: 17px; }

  .contact-shapes { position: absolute; inset: 0; }

  .holder {
    position: absolute; left: 18px; top: 118px; width: 150px;
    text-align: right; color: var(--ink-light);
  }
  .holder__name { font-size: 15px; font-weight: 500; letter-spacing: .08em; }
  .holder__role { font-size: 10.5px; letter-spacing: .06em; margin-bottom: 10px; }
  .holder__address { font-size: 10.5px; line-height: 1.5; letter-spacing: .04em; }

  .divider {
    position: absolute; left: 180px; top: 118px; width: 1px; height: 96px;
    background: rgba(255,255,255,.7);
  }

  .contact-list {
    position: absolute; left: 192px; top: 118px; list-style: none;
    color: var(--ink-light); font-size: 10.5px; letter-spacing: .05em;
  }
  .contact-list li { display: flex; align-items: center; gap: 6px; height: 19px; }
  .contact-list svg { width: 12px; height: 12px; flex: none; }
</style>
</head>
<body>
<main class="sheet">

  <section class="card card--brand" aria-label="Card front">
    <div class="brand-mark">
      <span class="brand-mark__dot"></span>
      <span class="brand-mark__name">Braven<br>Powerline Services</span>
    </div>
  </section>

  <section class="card card--contact" aria-label="Card back">
    <svg class="contact-shapes" viewBox="0 0 540 309" preserveAspectRatio="none" aria-hidden="true">
      <path d="M330,0 L372,0 C402,90 425,200 480,309 L438,309 C385,200 362,90 330,0 Z" fill="var(--silver)"/>
      <path d="M0,0 L320,0 C355,90 378,200 432,309 L0,309 Z" fill="var(--electric-blue)"/>
    </svg>

    <div class="holder">
      <p class="holder__name">Dalen Voskic</p>
      <p class="holder__role">Owner / C.E.O</p>
      <p class="holder__address">Suite # 214, Kel Bldg,<br>NY 40571<br>EC40923</p>
    </div>

    <span class="divider"></span>

    <ul class="contact-list">
      <li>
        <svg viewBox="0 0 12 12"><circle cx="6" cy="6" r="6" fill="#fff"/><path d="M4 3.2l1 1.4-.6.7c.4.9 1 1.5 1.9 1.9l.7-.6 1.4 1-.5 1.1C5.8 8.6 3.4 6.2 3 4z" fill="var(--electric-blue)"/></svg>
        0417 358 942
      </li>
      <li>
        <svg viewBox="0 0 12 12"><circle cx="6" cy="6" r="6" fill="#fff"/><path d="M4 3.2l1 1.4-.6.7c.4.9 1 1.5 1.9 1.9l.7-.6 1.4 1-.5 1.1C5.8 8.6 3.4 6.2 3 4z" fill="var(--electric-blue)"/></svg>
        0417 358 943
      </li>
      <li>
        <svg viewBox="0 0 12 12"><circle cx="6" cy="6" r="6" fill="#fff"/><path d="M4 3.2l1 1.4-.6.7c.4.9 1 1.5 1.9 1.9l.7-.6 1.4 1-.5 1.1C5.8 8.6 3.4 6.2 3 4z" fill="var(--electric-blue)"/></svg>
        0417 358 944
      </li>
      <li>
        <svg viewBox="0 0 12 12"><circle cx="6" cy="6" r="6" fill="#fff"/><rect x="3" y="4" width="6" height="4.2" fill="none" stroke="var(--electric-blue)" stroke-width=".9"/><path d="M3 4l3 2.3L9 4" fill="none" stroke="var(--electric-blue)" stroke-width=".9"/></svg>
        dalen@bravenpowerline.com
      </li>
      <li>
        <svg viewBox="0 0 12 12"><circle cx="6" cy="6" r="6" fill="#fff"/><circle cx="6" cy="6" r="3" fill="none" stroke="var(--electric-blue)" stroke-width=".8"/><path d="M3 6h6M6 3c-1.4 1.6-1.4 4.4 0 6M6 3c1.4 1.6 1.4 4.4 0 6" fill="none" stroke="var(--electric-blue)" stroke-width=".7"/></svg>
        www.bravenpowerline.com
      </li>
    </ul>

    <div class="brand-mark">
      <span class="brand-mark__dot"></span>
      <span class="brand-mark__name">Braven<br>Powerline<br>Services</span>
    </div>
  </section>

</main>
</body>
</html>
```